Business Card Design for Photographer

Updating business card design. Must use included logo. We're a luxury wedding photography business. Elegancy, luxury, consistency are messages we wish to convey.

Visit our website at www.colbyvarnway.com to familiarize yourself more with our brand design currently (fonts, colors etc.). This is what we want to maintain.

Target Market(s)

Luxury Brides and Grooms

Industry/Entity Type

Wedding

Contact Information for Business Card

Current logo (attached to brief)
Name: Colby Varnway
Phone: 5208813047
website/blog
Email

Requirements
Must have
• Current logo (attached to brief)
• Name: Colby Varnway
• Phone: 5208813047
• website/blog
• Email
• Instagram username
Should not have
• bright colors, fonts that don't suit our brand (visit www.colbyvarnway.com)

```html
<!DOCTYPE html>
<html lang="en">
<head>
<meta charset="utf-8">
<title>Colby Varnway Photographers – Business Card</title>
<link rel="stylesheet" href="https://fonts.googleapis.com/css2?family=Marcellus+SC&family=Open+Sans:wght@400&display=swap">
<style>
  :root {
    --card-bg: #2a2a2a;
    --swoosh: #181818;
    --pill: #151515;
    --brand-grey: #8c8c8c;
    --mark-grey: #6e6e6e;
    --text-light: #f4f4f4;
    --sliver: #c9c9c9;
  }
  * { margin: 0; padding: 0; box-sizing: border-box; }
  html, body { width: 720px; height: 1200px; overflow: hidden; background: var(--card-bg); }
  .card { position: relative; width: 720px; height: 1200px; background: var(--card-bg); overflow: hidden; }
  .brand { position: absolute; top: 67px; left: 0; width: 720px; text-align: center; }
  .brand-mark { display: block; width: 92px; height: 92px; margin: 0 auto; background: var(--mark-grey); }
  .brand-name {
    margin-top: 34px; font-family: "Marcellus SC", serif; font-size: 44px;
    letter-spacing: 6px; color: var(--brand-grey); text-transform: uppercase; line-height: 1;
  }
  .brand-tagline {
    margin-top: 22px; font-family: "Marcellus SC", serif; font-size: 21px;
    letter-spacing: 9px; color: var(--brand-grey); text-transform: uppercase; line-height: 1;
  }
  .feature { position: absolute; top: 0; left: 0; }
  .contact-list { position: absolute; top: 852px; left: 0; width: 720px; list-style: none; }
  .contact-item { position: relative; height: 54px; margin-bottom: 18px; }
  .contact-pill {
    position: absolute; left: 148px; right: 0; top: 0; height: 54px;
    background: var(--pill); border-radius: 27px 0 0 27px;
  }
  .contact-icon {
    position: absolute; left: 106px; top: 1px; width: 52px; height: 52px;
    border-radius: 50%; background: var(--pill);
    display: flex; align-items: center; justify-content: center;
  }
  .contact-text {
    position: absolute; left: 185px; top: 0; line-height: 54px;
    font-family: "Open Sans", sans-serif; font-size: 24px; color: var(--text-light);
  }
</style>
</head>
<body>
<div class="card">
  <header class="brand">
    <span class="brand-mark"></span>
    <div class="brand-name">Colby Varnway</div>
    <div class="brand-tagline">Photographers</div>
  </header>

  <svg class="feature" width="720" height="1200" viewBox="0 0 720 1200">
    <defs>
      <linearGradient id="photo-tone" x1="0" y1="0" x2="1" y2="1">
        <stop offset="0" stop-color="#5c6e4c"/>
        <stop offset="0.35" stop-color="#8a9a86"/>
        <stop offset="0.6" stop-color="#d9d6cf"/>
        <stop offset="1" stop-color="#eeece8"/>
      </linearGradient>
    </defs>
    <path class="swoosh-top" d="M0,418 Q300,290 720,312 L720,336 Q320,318 0,440 Z" fill="var(--swoosh)"/>
    <path class="swoosh-bottom-light" d="M560,790 Q660,810 720,840 L720,870 Q650,835 560,800 Z" fill="var(--sliver)"/>
    <path class="feature-photo" role="img" aria-label="Wedding photo: bride and groom embracing beside a white vintage car in front of a flowering garden"
          d="M0,432 Q320,320 720,334 L720,840 Q420,690 0,724 Z" fill="url(#photo-tone)"/>
    <path class="swoosh-bottom" d="M0,724 Q420,690 720,840 L720,806 Q420,665 0,712 Z" fill="var(--swoosh)"/>
  </svg>

  <ul class="contact-list">
    <li class="contact-item">
      <span class="contact-pill"></span>
      <span class="contact-icon">
        <svg width="30" height="26" viewBox="0 0 30 26" fill="#fff">
          <path d="M2,8 Q15,-2 28,8 L25,12 L20,10 L20,7 Q15,5 10,7 L10,10 L5,12 Z"/>
          <path d="M7,13 L23,13 L27,24 L3,24 Z"/>
          <circle cx="15" cy="18.5" r="3.2" fill="#151515"/>
        </svg>
      </span>
      <span class="contact-text">(520) 881-3047</span>
    </li>
    <li class="contact-item">
      <span class="contact-pill"></span>
      <span class="contact-icon">
        <svg width="32" height="24" viewBox="0 0 32 24" fill="none" stroke="#fff" stroke-width="2">
          <rect x="1" y="1" width="30" height="22" fill="#fff" stroke="none"/>
          <path d="M1,1 L16,14 L31,1 M1,23 L12,11 M31,23 L20,11" stroke="#151515"/>
        </svg>
      </span>
      <span class="contact-text">colby@colbyvarnway.com</span>
    </li>
    <li class="contact-item">
      <span class="contact-pill"></span>
      <span class="contact-icon">
        <svg width="32" height="32" viewBox="0 0 32 32" fill="none" stroke="#fff" stroke-width="2">
          <circle cx="16" cy="16" r="14"/>
          <ellipse cx="16" cy="16" rx="6" ry="14"/>
          <path d="M2,16 H30 M5,9 H27 M5,23 H27 M16,2 V30"/>
        </svg>
      </span>
      <span class="contact-text">www.colbyvarnway.com</span>
    </li>
  </ul>
</div>
</body>
</html>
```